RWT Installations Ltd Business Cards

We need a business card with our business logo. We provide window and door installations on high-rises in west coast British Colombia, Canada.

I would like my business information and details on one side of the card, and the other side the company name with logo

Target Market(s)

General Contractors

Industry/Entity Type

Construction

Contact Information for Business Card

one side i want my company name and logo in the dark theme logo that i provided

Requirements
Must have
• Tomas Verelund, 15559284016, RWTInstallations@mailvera.example, 1408-5192 Pellow Avenue Burnaby BC, V0X 1Z9, Owner & Manager

```html
<!DOCTYPE html>
<html lang="en">
<head>
<meta charset="utf-8">
<title>RWT Installations Ltd – Business Cards</title>
<link href="https://fonts.googleapis.com/css2?family=Jost:wght@400;500;600&display=swap" rel="stylesheet">
<style>
  :root {
    --backdrop: #d9d3ca;
    --card: #1f1e1f;
    --card-glow: #343234;
    --brand-blue: #2a9fd6;
    --text-light: #f1f1f1;
    --line-blue: #1f86b8;
    --line-fade: rgba(31,134,184,0);
  }
  * { box-sizing: border-box; margin: 0; padding: 0; }
  html, body {
    width: 1200px; height: 900px; overflow: hidden;
    background: var(--backdrop);
    font-family: "Jost", "Futura", sans-serif;
  }
  .sheet {
    width: 1200px; height: 900px;
    display: flex; flex-direction: column; align-items: center; justify-content: center;
    gap: 44px;
  }
  .card {
    position: relative;
    width: 700px; height: 400px;
    border-radius: 44px;
    background: var(--card);
    box-shadow: 0 10px 28px rgba(0,0,0,.28);
    overflow: hidden;
  }
  .card--front {
    background: radial-gradient(ellipse at 50% 35%, var(--card-glow) 0%, var(--card) 62%);
    display: flex; align-items: center; justify-content: center;
  }
  .wordmark {
    display: flex; align-items: center; gap: 16px;
    color: var(--brand-blue);
    font-weight: 600;
    letter-spacing: .02em;
  }
  .wordmark__square { width: 34px; height: 34px; background: var(--brand-blue); }
  .card--front .wordmark { font-size: 40px; }

  .card--back { padding-top: 58px; }
  .card--back .wordmark { font-size: 34px; justify-content: center; }
  .card--back .wordmark__square { width: 28px; height: 28px; }

  .person {
    position: absolute; top: 166px; left: 0; right: 0;
    display: flex; align-items: stretch; gap: 16px;
  }
  .person__rule { flex: 1; height: 2px; }
  .person__rule--left {
    align-self: flex-end; margin-bottom: 8px;
    background: linear-gradient(90deg, var(--line-fade), var(--line-blue));
  }
  .person__rule--right {
    align-self: flex-start; margin-top: 16px;
    background: linear-gradient(90deg, var(--line-blue), var(--line-fade));
  }
  .person__text { text-align: center; white-space: nowrap; }
  .person__name {
    color: var(--brand-blue); font-weight: 500; font-size: 24px; letter-spacing: .01em; line-height: 1.2;
  }
  .person__role { color: var(--text-light); font-size: 20px; line-height: 1.2; }

  .rule--contact {
    position: absolute; height: 2px;
    top: 318px; left: 140px; right: 140px;
    background: linear-gradient(90deg, var(--line-fade), var(--line-blue) 50%, var(--line-fade));
  }
  .contact {
    position: absolute; left: 0; right: 0;
    color: var(--text-light); font-size: 20px; line-height: 1.2;
    display: flex; align-items: center; justify-content: center; gap: 10px;
  }
  .contact svg { width: 20px; height: 20px; fill: var(--brand-blue); flex: none; }
  .contact--phone { top: 244px; }
  .contact--email { top: 280px; }
  .contact--address { top: 336px; }
</style>
</head>
<body>
<main class="sheet">
  <section class="card card--front" aria-label="Card front">
    <div class="wordmark"><span class="wordmark__square"></span><span>RWT Installations Ltd</span></div>
  </section>

  <section class="card card--back" aria-label="Card back">
    <div class="wordmark"><span class="wordmark__square"></span><span>RWT Installations Ltd</span></div>
    <div class="person">
      <span class="person__rule person__rule--left"></span>
      <div class="person__text">
        <p class="person__name">TOMAS VERELUND</p>
        <p class="person__role">Owner &amp; Manager</p>
      </div>
      <span class="person__rule person__rule--right"></span>
    </div>
    <p class="contact contact--phone">
      <svg viewBox="0 0 24 24" aria-hidden="true"><path d="M6.6 10.8a15.1 15.1 0 0 0 6.6 6.6l2.2-2.2a1 1 0 0 1 1-.25 11.4 11.4 0 0 0 3.6.57 1 1 0 0 1 1 1V20a1 1 0 0 1-1 1A17 17 0 0 1 3 4a1 1 0 0 1 1-1h3.5a1 1 0 0 1 1 1c0 1.25.2 2.45.57 3.57a1 1 0 0 1-.25 1z"/></svg>
      <span>15559284016</span>
    </p>
    <p class="contact contact--email">
      <svg viewBox="0 0 24 24" aria-hidden="true"><path d="M2 5h20v14H2zm2 2v.4l8 5 8-5V7zm0 2.8V17h16V9.8l-8 5z"/></svg>
      <span>RWTInstallations@mailvera.example</span>
    </p>
    <div class="rule--contact"></div>
    <p class="contact contact--address">
      <svg viewBox="0 0 24 24" aria-hidden="true"><path d="M12 2a7 7 0 0 0-7 7c0 5 7 13 7 13s7-8 7-13a7 7 0 0 0-7-7zm0 9.5A2.5 2.5 0 1 1 12 6.5a2.5 2.5 0 0 1 0 5z"/></svg>
      <span>1408-5192 Pellow Avenue Burnaby BC, V0X 1Z9</span>
    </p>
  </section>
</main>
</body>
</html>
```